Construction Project Management Introductory Brochure

Design a multi page brochure to send to clients primarily through email as an introduction to my company. It should give a background on myself/company, our services and markets we serve. I am looking for experienced designs in brochures to provide direction on content. Website is www.tallowcrest.com to use as background knowledge. Service categories include: Project Management, Construction Administration, Move Management and Cost Estimating. I included a post card recently developed in the files to show existing marketing material and current logo. company slogan: Your plans in our hands. In my experience on this website, the first submissions let me make the decision on which designer to work with based on layout and design. Then we can add the correct content. Thanks! Looking to wrap this up quickly.

Target Market(s)

Academic (all ages of educational buildings), Residential, Hospitality (Restaurants and hotels), Commercial office buildings, Government Projects - All interior fit outs.

Industry/Entity Type

Construction

Font styles to use
Serif

Colors
33b8a4
00a990
86cfc6
cfeae6
edf8f6
ffffff
000000
757575
cbcbcb

Requirements
Must have
• About us section
• Services section with detailed list
• WBE logo
• I included my old old document as a horrible sample. But what it does have is a break down of project management services listed.
Nice to have
• The three documents with the word "proposal" in the front are most up to date and preferred for reference. stock photos. You do not have to use the exact photos from my website. I would like your added suggestions.

```html
<!DOCTYPE html>
<html lang="en">
<head>
<meta charset="utf-8">
<title>Tallowcrest Project Management – Brochure Back Cover</title>
<link rel="stylesheet" href="https://fonts.googleapis.com/css2?family=Cormorant+Garamond:wght@600&family=Open+Sans:wght@400;600&display=swap">
<style>
  :root {
    --teal: #33b8a4;
    --teal-deep: #00a990;
    --teal-soft: #86cfc6;
    --teal-pale: #cfeae6;
    --teal-mist: #edf8f6;
    --white: #ffffff;
    --black: #000000;
    --grey: #757575;
    --grey-light: #cbcbcb;
  }
  * { margin: 0; padding: 0; box-sizing: border-box; }
  html, body { width: 1200px; height: 900px; overflow: hidden; background: var(--white); }
  .back-cover {
    position: relative;
    width: 1200px;
    height: 900px;
    overflow: hidden;
    background: linear-gradient(100deg, var(--teal) 0%, #3fc2b0 55%, #6fd3c7 100%);
    font-family: "Open Sans", sans-serif;
    color: var(--white);
  }
  .soft-arc {
    position: absolute;
    left: 360px; top: 60px;
    width: 800px; height: 540px;
    border-radius: 50%;
    border: 60px solid rgba(255,255,255,0.05);
  }
  .skyline-band {
    position: absolute;
    left: 0; right: 0; bottom: 0;
    height: 420px;
    background:
      linear-gradient(90deg, rgba(20,140,120,0.18) 0%, rgba(20,140,120,0.08) 60%, rgba(20,140,120,0) 100%),
      linear-gradient(180deg, rgba(0,169,144,0) 0%, rgba(0,150,128,0.18) 45%, rgba(20,140,120,0.28) 100%);
  }
  .feature-photo {
    position: absolute;
    left: 420px; top: 150px;
    width: 380px; height: 380px;
    border-radius: 50%;
    border: 5px solid var(--white);
    background: linear-gradient(180deg, #aec4dc 0%, #c9cbd6 45%, #d8c4b0 68%, #7d8488 100%);
  }
  .contact-strip {
    position: absolute;
    left: 70px; top: 640px;
    display: flex;
    align-items: flex-start;
  }
  .brand {
    display: flex;
    align-items: center;
    gap: 12px;
    padding-top: 14px;
    padding-right: 30px;
  }
  .brand-dot {
    width: 30px; height: 30px;
    border-radius: 50%;
    background: var(--white);
  }
  .brand-name {
    font-family: "Cormorant Garamond", serif;
    font-weight: 600;
    font-size: 32px;
    letter-spacing: 1px;
    color: var(--white);
  }
  .divider {
    width: 1.5px; height: 80px;
    background: rgba(255,255,255,0.75);
    margin-right: 26px;
  }
  .contact-col { margin-right: 40px; font-size: 11px; line-height: 1.5; white-space: nowrap; }
  .contact-col .label { font-weight: 600; }
  .contact-col .value { opacity: 0.85; }
  .contact-col .group + .group { margin-top: 8px; }
  .certification-corner {
    position: absolute;
    right: -60px; bottom: -60px;
    width: 260px; height: 260px;
    border-radius: 50%;
    background: var(--white);
  }
  .certification-badge {
    position: absolute;
    right: 40px; bottom: 50px;
    width: 110px; height: 72px;
    border-radius: 8px;
    background: var(--teal-pale);
  }
</style>
</head>
<body>
  <section class="back-cover">
    <div class="soft-arc"></div>
    <div class="skyline-band" role="img" aria-label="Faint city skyline photograph blended into the teal background"></div>

    <div class="feature-photo" role="img" aria-label="Photograph of a tall observation tower rising above a city skyline at dusk"></div>

    <div class="contact-strip">
      <div class="brand">
        <span class="brand-dot"></span>
        <span class="brand-name">TALLOWCREST</span>
      </div>
      <div class="divider"></div>
      <div class="contact-col">
        <div class="label">Address:</div>
        <div class="value">Tallowcrest Project Management<br>2140 Harbor Lane, Suite 210<br>Riverton, NV 89000</div>
      </div>
      <div class="contact-col">
        <div class="group">
          <div class="label">Mobile:</div>
          <div class="value">(555) 014-2290</div>
        </div>
        <div class="group">
          <div class="label">Office:</div>
          <div class="value">(555) 014-7731</div>
        </div>
      </div>
      <div class="contact-col">
        <div class="group">
          <div class="label">E-mail:</div>
          <div class="value">info@tallowcrest.com</div>
        </div>
        <div class="group">
          <div class="label">Website:</div>
          <div class="value">www.tallowcrest.com</div>
        </div>
      </div>
    </div>

    <div class="certification-corner"></div>
    <div class="certification-badge" role="img" aria-label="Women-owned business certification badge"></div>
  </section>
</body>
</html>
```